SIGN UP PAGE AND CHECK OUT PROCESS DESIGN NEEDED

I offer a subscription service. Two products that offer the same exact features just two different prices as the cheaper product offers limited of all the features....<br/><br/>PLEASE USE EXISTING THEME OF CURRENT DESIGN JUST MAKE AN IMPROVED SIGN UP PAGE. <br/><br/><br/>NEED SIGN UP PAGE for a subscription service..... <br/>This is my current sign up page, only offers one product: https://www.brightpromoperks.example/?page=signup <br/><br/>Please use all the same fields and content listed on this sign up page also please do a fake sign up to see the credit card page. I also need the credit card page to be designed....or if you want to combine the sign up and credit card page, etc. all in one I am open for that too....my goal is a super quick an easy sign up for customer. <br/><br/> AL A CARTE PROGRAM<br/>1 CERTIFICATE TYPE EACH MONTH<br/>$49/MTH MONTH TO MONTH BASIS NO CONTRACTS<br/>$239 ONE TIME PAYMENT FOR 6 MTHS OF SERVICE<br/>$399 ONE TIME PAYMENT FOR 12 MONTHS OF SERVICE<br/><br/>FEATURES:<br/><br/>UNLIMITED CERTIFICATE PDF DOWNLOADS<br/><br/>UNLIMITED E-MAIL CERTIFICATES<br/><br/>UNLIMITED TEXT/SMS CERTIFICATES<br/><br/>UNLIMITED API USAGE<br/><br/>UNLIMITED WEB BANNER CERTIFICATES<br/><br/>FULL REDEMPTION TRACKING<br/><br/>CERTIFICATE DISTRIBUTION REPORTS<br/><br/>WHITE LABEL REDEMPTION SITE<br/><br/>END USER MARKETING VIDEOS<br/><br/>MARKETING POSTERS AND FLYERS<br/><br/>PRODUCT DESCRIPTIONI BROCHURES<br/><br/>THE LATEST TIPS<br/><br/>SEPERATE REDEMPTION WEBSITES<br/><br/>CONTACT US 24/7<br/><br/>AFFILIATE PROGRAM<br/><br/>DISCOUNT TRAVEL BOOKING ENGINE<br/><br/>UNLIMITED PROGRAM<br/>UNLIMITED AMOUNTS OF ALL THE CERTIFICATES<br/>$99/MTH MONTH TO MONTH BASIS NO CONTRACTS<br/>$495 ONE TIME PAYMENT FOR 6 MTHS OF SERVICE<br/>$2,295 ONE TIME PAYMENT FOR 12 MONTHS OF SERVICE<br/><br/>FEATURES:<br/><br/>UNLIMITED CERTIFICATE PDF DOWNLOADS<br/><br/>UNLIMITED E-MAIL CERTIFICATES<br/><br/>UNLIMITED TEXT/SMS CERTIFICATES<br/><br/>UNLIMITED API USAGE<br/><br/>UNLIMITED WEB BANNER CERTIFICATES<br/><br/>FULL REDEMPTION TRACKING<br/><br/>CERTIFICATE DISTRIBUTION REPORTS<br/><br/>WHITE LABEL REDEMPTION SITE<br/><br/>END USER MARKETING VIDEOS<br/><br/>MARKETING POSTERS AND FLYERS<br/><br/>PRODUCT DESCRIPTIONI BROCHURES<br/><br/>THE LATEST TIPS<br/><br/>SEPERATE REDEMPTION WEBSITES<br/><br/>CONTACT US 24/7<br/><br/>AFFILIATE PROGRAM<br/><br/>DISCOUNT TRAVEL BOOKING ENGINE<br/><br/><br/>

Target Market(s)

B2B SMALL BUSINESS OWNERS
MARKETERS
ADVERTISERS

Industry/Entity Type

Digital Marketing

Number of Pages Required

3 page

Colors

Designer to choose colors to be used in the design.

Requirements
Must have
• MUST MATCH EXISTING THEME
Nice to have
• A VERY MODERN DESIGN

```html
<!DOCTYPE html>
<html lang="en">
<head>
<meta charset="utf-8">
<title>Sign Up – Bright Promo Perks</title>
<link href="https://fonts.googleapis.com/css2?family=Open+Sans:wght@400;600;700&display=swap" rel="stylesheet">
<style>
:root{
  --brand:#1560b4;
  --ink:#222;
  --panel:#ececec;
  --line:#c9c9c9;
  --nav-active:#1d1d1d;
  --footer:#0b0b0b;
  --footer-text:#9a9a9a;
  --white:#fff;
}
*{box-sizing:border-box;margin:0;padding:0}
html,body{width:1200px;height:2347px;overflow:hidden}
body{font-family:"Open Sans",Arial,sans-serif;color:var(--ink);background:var(--white)}
.wrap{width:911px;margin:0 auto;position:relative}

/* header */
.site-header{height:82px}
.site-header .wrap{display:flex;justify-content:space-between;align-items:center;height:82px}
.brand{display:flex;align-items:center;gap:10px;color:var(--brand);font-weight:700;font-size:24px;letter-spacing:.5px}
.brand-mark{width:30px;height:30px;background:var(--brand)}
.contact-top{display:flex;align-items:center;gap:12px}
.contact-top p{text-align:right;font-size:15px;line-height:21px;color:#444}
.contact-top b{color:var(--ink);font-weight:600}
.phone-btn{width:35px;height:35px;background:var(--brand);border-radius:3px;display:flex;align-items:center;justify-content:center}

.main-nav{background:var(--brand);height:40px}
.main-nav ul{list-style:none;position:relative;height:40px}
.main-nav li{position:absolute;top:0;color:var(--white);font-size:13px;font-weight:600;line-height:40px;white-space:nowrap}
.main-nav li.active{left:0;width:112px;text-align:center;background:var(--nav-active)}
.main-nav li:nth-child(2){left:141px}
.main-nav li:nth-child(3){left:311px}
.main-nav li:nth-child(4){left:434px}
.main-nav li:nth-child(5){left:567px}
.main-nav li:nth-child(6){left:724px}
.main-nav li:nth-child(7){left:816px}

/* plans */
.plans{padding-top:40px;height:1019px}
.plans .wrap{display:flex;justify-content:space-between}
.plan{width:432px;height:898px;background:var(--panel);padding:26px 32px}
.plan h2{color:var(--brand);font-size:33px;font-weight:700;line-height:40px}
.plan .sub{font-size:20px;line-height:24px;margin-top:6px;height:74px}
.prices{display:flex;gap:4px;margin-top:8px}
.price{width:120px;height:143px;background:var(--white);border:1px solid var(--line);border-radius:2px;text-align:center;padding-top:11px}
.price.selected{background:var(--brand);border-color:var(--brand)}
.price .amt{color:var(--brand);font-size:31px;font-weight:700;line-height:40px;white-space:nowrap}
.price .amt sup{font-size:19px;vertical-align:14px;margin-right:1px}
.price .note{font-size:9.5px;line-height:16px;color:#333;margin-top:10px;padding:0 8px}
.price.selected .amt{color:var(--white)}
.price.selected .note{color:#b8d2ef}
.plan h3{font-size:20px;font-weight:400;margin-top:28px;line-height:24px}
.features{list-style:none;margin-top:13px}
.features li{display:flex;align-items:center;gap:10px;font-size:13.5px;height:32px;white-space:nowrap}

/* signup */
.signup{height:749px;background:linear-gradient(180deg,#0f4f98 0%,#0d3f78 45%,#0b2647 100%);color:var(--white);text-align:center;padding-top:68px}
.signup h2{font-size:40px;font-weight:600;line-height:50px}
.intro-box{border:1px solid #7ea9db;margin-top:16px;padding:10px 14px;font-size:12.5px;line-height:19px;color:#a9c7ea}
.charge{font-size:12.5px;line-height:21px;color:#c9dbef;margin-top:19px;margin-left:-4px;margin-right:-4px}
.notice{font-size:14.5px;font-weight:600;margin-top:16px;white-space:nowrap;letter-spacing:-.1px}
.signup-form{width:879px;margin:21px auto 0;display:grid;grid-template-columns:repeat(4,209px);column-gap:15px;row-gap:16px}
.field{height:40px;background:var(--white);color:#666;font-size:13px;text-align:left;padding:0 16px;display:flex;align-items:center;justify-content:space-between}
.field.wide{grid-column:1/5}
.btn-signup{display:inline-block;margin-top:19px;background:var(--brand);color:var(--white);font-size:16px;font-weight:600;height:40px;line-height:40px;width:136px}

/* footer */
.site-footer{background:var(--footer);height:400px;padding-top:57px;color:var(--footer-text)}
.site-footer .wrap{display:flex}
.site-footer h4{color:var(--white);font-size:19px;font-weight:600;line-height:24px;white-space:nowrap}
.quick{width:438px}
.quick .cols{display:flex;margin-top:17px}
.quick ul{list-style:none;font-size:12px;line-height:32px;white-space:nowrap}
.quick ul:first-child{width:144px}
.details{width:331px}
.details .item{display:flex;gap:14px;font-size:12px;line-height:18px;margin-top:20px}
.details .item:first-of-type{margin-top:23px}
.social .icons{display:grid;grid-template-columns:40px 40px;gap:16px;margin-top:24px;margin-left:2px}
.social .icons span{width:40px;height:40px;border:1px solid #777;border-radius:50%}
.copyright{background:#1b1b1b;height:57px;text-align:center;font-size:12px;line-height:57px;color:#8a8a8a}
</style>
</head>
<body>

<header class="site-header">
  <div class="wrap">
    <div class="brand"><span class="brand-mark"></span>BRIGHT PROMO PERKS</div>
    <div class="contact-top">
      <p>USA Office : <b>555-014-2290</b><br>International : <b>1-800-555-0173</b></p>
      <span class="phone-btn"><svg width="16" height="16" viewBox="0 0 24 24"><path fill="#fff" d="M6.6 10.8c1.4 2.8 3.8 5.1 6.6 6.6l2.2-2.2c.3-.3.7-.4 1-.2 1.1.4 2.3.6 3.6.6.6 0 1 .4 1 1V20c0 .6-.4 1-1 1C10.6 21 3 13.4 3 4c0-.6.4-1 1-1h3.5c.6 0 1 .4 1 1 0 1.3.2 2.5.6 3.6.1.3 0 .7-.2 1z"/></svg></span>
    </div>
  </div>
</header>

<nav class="main-nav">
  <div class="wrap">
    <ul>
      <li class="active">HOME</li><li>OUR INCENTIVES</li><li>SAMPLES</li><li>AFFILIATES</li><li>TESTIMONIALS</li><li>FAQ</li><li>CONTACT</li>
    </ul>
  </div>
</nav>

<section class="plans">
  <div class="wrap">
    <article class="plan">
      <h2>AL A CARTE PROGRAM</h2>
      <p class="sub">1 CERTIFICATE TYPE EACH MONTH</p>
      <div class="prices">
        <div class="price selected"><div class="amt"><sup>$</sup>49</div><p class="note">PER MONTH<br>MONTH TO<br>MONTH BASIS<br>NO CONTRACTS</p></div>
        <div class="price"><div class="amt"><sup>$</sup>239</div><p class="note">ONE TIME<br>PAYMENT FOR 6<br>MTHS OF SERVICE</p></div>
        <div class="price"><div class="amt"><sup>$</sup>399</div><p class="note">ONE TIME<br>PAYMENT FOR 12<br>MONTHS OF<br>SERVICE</p></div>
      </div>
      <h3>FEATURES :</h3>
      <ul class="features">
        <li><svg width="12" height="12" viewBox="0 0 12 12"><circle cx="6" cy="6" r="6" fill="#444"/><path d="M3.3 6.1l1.8 1.8 3.6-3.6" stroke="#fff" stroke-width="1.5" fill="none"/></svg>UNLIMITED CERTIFICATE PDF DOWNLOADS</li>
        <li><svg width="12" height="12" viewBox="0 0 12 12"><circle cx="6" cy="6" r="6" fill="#444"/><path d="M3.3 6.1l1.8 1.8 3.6-3.6" stroke="#fff" stroke-width="1.5" fill="none"/></svg>UNLIMITED E-MAIL CERTIFICATES</li>
        <li><svg width="12" height="12" viewBox="0 0 12 12"><circle cx="6" cy="6" r="6" fill="#444"/><path d="M3.3 6.1l1.8 1.8 3.6-3.6" stroke="#fff" stroke-width="1.5" fill="none"/></svg>UNLIMITED TEXT/SMS CERTIFICATES</li>
        <li><svg width="12" height="12" viewBox="0 0 12 12"><circle cx="6" cy="6" r="6" fill="#444"/><path d="M3.3 6.1l1.8 1.8 3.6-3.6" stroke="#fff" stroke-width="1.5" fill="none"/></svg>UNLIMITED API USAGE</li>
        <li><svg width="12" height="12" viewBox="0 0 12 12"><circle cx="6" cy="6" r="6" fill="#444"/><path d="M3.3 6.1l1.8 1.8 3.6-3.6" stroke="#fff" stroke-width="1.5" fill="none"/></svg>UNLIMITED WEB BANNER CERTIFICATES</li>
        <li><svg width="12" height="12" viewBox="0 0 12 12"><circle cx="6" cy="6" r="6" fill="#444"/><path d="M3.3 6.1l1.8 1.8 3.6-3.6" stroke="#fff" stroke-width="1.5" fill="none"/></svg>FULL REDEMPTION TRACKING</li>
        <li><svg width="12" height="12" viewBox="0 0 12 12"><circle cx="6" cy="6" r="6" fill="#444"/><path d="M3.3 6.1l1.8 1.8 3.6-3.6" stroke="#fff" stroke-width="1.5" fill="none"/></svg>CERTIFICATE DISTRIBUTION REPORTS</li>
        <li><svg width="12" height="12" viewBox="0 0 12 12"><circle cx="6" cy="6" r="6" fill="#444"/><path d="M3.3 6.1l1.8 1.8 3.6-3.6" stroke="#fff" stroke-width="1.5" fill="none"/></svg>WHITE LABEL REDEMPTION SITE</li>
        <li><svg width="12" height="12" viewBox="0 0 12 12"><circle cx="6" cy="6" r="6" fill="#444"/><path d="M3.3 6.1l1.8 1.8 3.6-3.6" stroke="#fff" stroke-width="1.5" fill="none"/></svg>END USER MARKETING VIDEOS</li>
        <li><svg width="12" height="12" viewBox="0 0 12 12"><circle cx="6" cy="6" r="6" fill="#444"/><path d="M3.3 6.1l1.8 1.8 3.6-3.6" stroke="#fff" stroke-width="1.5" fill="none"/></svg>MARKETING POSTERS AND FLYERS</li>
        <li><svg width="12" height="12" viewBox="0 0 12 12"><circle cx="6" cy="6" r="6" fill="#444"/><path d="M3.3 6.1l1.8 1.8 3.6-3.6" stroke="#fff" stroke-width="1.5" fill="none"/></svg>PRODUCT DESCRIPTIONI BROCHURES</li>
        <li><svg width="12" height="12" viewBox="0 0 12 12"><circle cx="6" cy="6" r="6" fill="#444"/><path d="M3.3 6.1l1.8 1.8 3.6-3.6" stroke="#fff" stroke-width="1.5" fill="none"/></svg>THE LATEST TIPS</li>
        <li><svg width="12" height="12" viewBox="0 0 12 12"><circle cx="6" cy="6" r="6" fill="#444"/><path d="M3.3 6.1l1.8 1.8 3.6-3.6" stroke="#fff" stroke-width="1.5" fill="none"/></svg>SEPERATE REDEMPTION WEBSITES</li>
        <li><svg width="12" height="12" viewBox="0 0 12 12"><circle cx="6" cy="6" r="6" fill="#444"/><path d="M3.3 6.1l1.8 1.8 3.6-3.6" stroke="#fff" stroke-width="1.5" fill="none"/></svg>CONTACT US 24/7</li>
        <li><svg width="12" height="12" viewBox="0 0 12 12"><circle cx="6" cy="6" r="6" fill="#444"/><path d="M3.3 6.1l1.8 1.8 3.6-3.6" stroke="#fff" stroke-width="1.5" fill="none"/></svg>AFFILIATE PROGRAM</li>
        <li><svg width="12" height="12" viewBox="0 0 12 12"><circle cx="6" cy="6" r="6" fill="#444"/><path d="M3.3 6.1l1.8 1.8 3.6-3.6" stroke="#fff" stroke-width="1.5" fill="none"/></svg>DISCOUNT TRAVEL BOOKING ENGINE</li>
      </ul>
    </article>

    <article class="plan">
      <h2>UNLIMITED PROGRAM</h2>
      <p class="sub">UNLIMITED AMOUNTS OF ALL THE CERTIFICATES</p>
      <div class="prices">
        <div class="price"><div class="amt"><sup>$</sup>99</div><p class="note">PER MONTH<br>MONTH TO<br>MONTH BASIS<br>NO CONTRACTS</p></div>
        <div class="price"><div class="amt"><sup>$</sup>495</div><p class="note">ONE TIME<br>PAYMENT FOR 6<br>MTHS OF SERVICE</p></div>
        <div class="price"><div class="amt"><sup>$</sup>2,295</div><p class="note">ONE TIME<br>PAYMENT FOR 12<br>MONTHS OF<br>SERVICE</p></div>
      </div>
      <h3>FEATURES :</h3>
      <ul class="features">
        <li><svg width="12" height="12" viewBox="0 0 12 12"><circle cx="6" cy="6" r="6" fill="#444"/><path d="M3.3 6.1l1.8 1.8 3.6-3.6" stroke="#fff" stroke-width="1.5" fill="none"/></svg>UNLIMITED CERTIFICATE PDF DOWNLOADS</li>
        <li><svg width="12" height="12" viewBox="0 0 12 12"><circle cx="6" cy="6" r="6" fill="#444"/><path d="M3.3 6.1l1.8 1.8 3.6-3.6" stroke="#fff" stroke-width="1.5" fill="none"/></svg>UNLIMITED E-MAIL CERTIFICATES</li>
        <li><svg width="12" height="12" viewBox="0 0 12 12"><circle cx="6" cy="6" r="6" fill="#444"/><path d="M3.3 6.1l1.8 1.8 3.6-3.6" stroke="#fff" stroke-width="1.5" fill="none"/></svg>UNLIMITED TEXT/SMS CERTIFICATES</li>
        <li><svg width="12" height="12" viewBox="0 0 12 12"><circle cx="6" cy="6" r="6" fill="#444"/><path d="M3.3 6.1l1.8 1.8 3.6-3.6" stroke="#fff" stroke-width="1.5" fill="none"/></svg>UNLIMITED API USAGE</li>
        <li><svg width="12" height="12" viewBox="0 0 12 12"><circle cx="6" cy="6" r="6" fill="#444"/><path d="M3.3 6.1l1.8 1.8 3.6-3.6" stroke="#fff" stroke-width="1.5" fill="none"/></svg>UNLIMITED WEB BANNER CERTIFICATES</li>
        <li><svg width="12" height="12" viewBox="0 0 12 12"><circle cx="6" cy="6" r="6" fill="#444"/><path d="M3.3 6.1l1.8 1.8 3.6-3.6" stroke="#fff" stroke-width="1.5" fill="none"/></svg>FULL REDEMPTION TRACKING</li>
        <li><svg width="12" height="12" viewBox="0 0 12 12"><circle cx="6" cy="6" r="6" fill="#444"/><path d="M3.3 6.1l1.8 1.8 3.6-3.6" stroke="#fff" stroke-width="1.5" fill="none"/></svg>CERTIFICATE DISTRIBUTION REPORTS</li>
        <li><svg width="12" height="12" viewBox="0 0 12 12"><circle cx="6" cy="6" r="6" fill="#444"/><path d="M3.3 6.1l1.8 1.8 3.6-3.6" stroke="#fff" stroke-width="1.5" fill="none"/></svg>WHITE LABEL REDEMPTION SITE</li>
        <li><svg width="12" height="12" viewBox="0 0 12 12"><circle cx="6" cy="6" r="6" fill="#444"/><path d="M3.3 6.1l1.8 1.8 3.6-3.6" stroke="#fff" stroke-width="1.5" fill="none"/></svg>END USER MARKETING VIDEOS</li>
        <li><svg width="12" height="12" viewBox="0 0 12 12"><circle cx="6" cy="6" r="6" fill="#444"/><path d="M3.3 6.1l1.8 1.8 3.6-3.6" stroke="#fff" stroke-width="1.5" fill="none"/></svg>MARKETING POSTERS AND FLYERS</li>
        <li><svg width="12" height="12" viewBox="0 0 12 12"><circle cx="6" cy="6" r="6" fill="#444"/><path d="M3.3 6.1l1.8 1.8 3.6-3.6" stroke="#fff" stroke-width="1.5" fill="none"/></svg>PRODUCT DESCRIPTIONI BROCHURES</li>
        <li><svg width="12" height="12" viewBox="0 0 12 12"><circle cx="6" cy="6" r="6" fill="#444"/><path d="M3.3 6.1l1.8 1.8 3.6-3.6" stroke="#fff" stroke-width="1.5" fill="none"/></svg>THE LATEST TIPS</li>
        <li><svg width="12" height="12" viewBox="0 0 12 12"><circle cx="6" cy="6" r="6" fill="#444"/><path d="M3.3 6.1l1.8 1.8 3.6-3.6" stroke="#fff" stroke-width="1.5" fill="none"/></svg>SEPERATE REDEMPTION WEBSITES</li>
        <li><svg width="12" height="12" viewBox="0 0 12 12"><circle cx="6" cy="6" r="6" fill="#444"/><path d="M3.3 6.1l1.8 1.8 3.6-3.6" stroke="#fff" stroke-width="1.5" fill="none"/></svg>CONTACT US 24/7</li>
        <li><svg width="12" height="12" viewBox="0 0 12 12"><circle cx="6" cy="6" r="6" fill="#444"/><path d="M3.3 6.1l1.8 1.8 3.6-3.6" stroke="#fff" stroke-width="1.5" fill="none"/></svg>AFFILIATE PROGRAM</li>
        <li><svg width="12" height="12" viewBox="0 0 12 12"><circle cx="6" cy="6" r="6" fill="#444"/><path d="M3.3 6.1l1.8 1.8 3.6-3.6" stroke="#fff" stroke-width="1.5" fill="none"/></svg>DISCOUNT TRAVEL BOOKING ENGINE</li>
      </ul>
    </article>
  </div>
</section>

<section class="signup">
  <div class="wrap">
    <h2>SIGN UP</h2>
    <p class="intro-box">Congratulations on making the decision to make more money for your business. This program is an online monthly subscription based incentive marketing system. You will be able to print and email an unlimited number of our certificates and you also get unlimited use of our certificate webite banners.</p>
    <p class="charge">Today you will be charged $99.00 plus a one-time set up fee of $99.00 for a grand total of $198.00 for your first month. You will also be set up on an automatic 30 day recurring billing cycle to be charged $99 every month until you submit a support ticket to cancel. You must submit a support ticket from your back end account at least 3 business days before your next billing date in order not be charged for the following month.</p>
    <p class="notice">**The information you provide below must match the billing details of where your billing statement is mailed to from your bank.</p>
    <div class="signup-form">
      <div class="field">First Name*</div>
      <div class="field">Last Name*</div>
      <div class="field">Company</div>
      <div class="field">Email Address*</div>
      <div class="field">Billing Address*</div>
      <div class="field">Billing Address 2</div>
      <div class="field">City</div>
      <div class="field">State*<svg width="13" height="8" viewBox="0 0 13 8"><path d="M1 1l5.5 5.5L12 1" stroke="#444" stroke-width="2" fill="none"/></svg></div>
      <div class="field">Country*<svg width="13" height="8" viewBox="0 0 13 8"><path d="M1 1l5.5 5.5L12 1" stroke="#444" stroke-width="2" fill="none"/></svg></div>
      <div class="field">Zip*</div>
      <div class="field">Phone*</div>
      <div class="field">Username*</div>
      <div class="field">Password*</div>
      <div class="field">Confirm Password*</div>
      <div class="field">Industry*</div>
      <div class="field">Promo Code</div>
      <div class="field wide">How Did You Hear About Us?*<svg width="13" height="8" viewBox="0 0 13 8"><path d="M1 1l5.5 5.5L12 1" stroke="#444" stroke-width="2" fill="none"/></svg></div>
    </div>
    <span class="btn-signup">SIGNUP NOW</span>
  </div>
</section>

<footer class="site-footer">
  <div class="wrap">
    <div class="quick">
      <h4>QUICK LINKS</h4>
      <div class="cols">
        <ul><li>Home</li><li>Our Incentives</li><li>Samples</li><li>Affiliate</li><li>Testimonials</li><li>Faq</li><li>Contact Us</li><li>Terms &amp; Conditions</li></ul>
        <ul><li>Privacy Policy</li><li>Hoteliers</li><li>BPP PDF Flyer</li><li>BPP PDF Brochure</li><li>BPP Certificates List</li><li>How To Use BPP Certificates</li><li>Free Video Ad Mock Up For Marketing</li></ul>
      </div>
    </div>
    <div class="details">
      <h4>CONTACT DETAILS</h4>
      <div class="item"><svg width="12" height="14" viewBox="0 0 12 16"><path fill="#888" d="M6 0a6 6 0 0 0-6 6c0 4.5 6 10 6 10s6-5.5 6-10a6 6 0 0 0-6-6zm0 8.5A2.5 2.5 0 1 1 6 3.5a2.5 2.5 0 0 1 0 5z"/></svg><p>Bright Promo Perks Group, Inc.<br>1450 Harbor View Lane<br>Bayside CA 90000</p></div>
      <div class="item"><svg width="12" height="14" viewBox="0 0 14 14"><rect x="1" y="2" width="12" height="11" fill="none" stroke="#888" stroke-width="1.5"/><path d="M1 5h12M4 0v3M10 0v3" stroke="#888" stroke-width="1.5"/></svg><p>Hours: Mon-Fri 8am - 5pm PST<br>Sat-Sun CLOSED</p></div>
    </div>
    <div class="social">
      <h4>FOLLOW US ON</h4>
      <div class="icons"><span></span><span></span><span></span><span></span></div>
    </div>
  </div>
</footer>
<div class="copyright">Copyright © 2020 Bright Promo Perks Group, Inc. All Rights Reserved.</div>

</body>
</html>
```